Australian Online Training Organisation needs a Website Design

We need a Web Design ideally using a Wordpress Divi template which will represent an Australian Online Training Company.

(Pendlow Online Training)

The website will represent a range of short courses with an emphasis on business, brightnet, leadership etc.

The website will 'shell out' to the third party portal where 'bookings' occur. I am imaging a fantastic looking web design with perhaps 5-6 pages.

I am wondering if a selection of courses including the below list can be incorporated?

The variety of courses include :

Workplace Safety
Sales Training
Leadership
Process Management
Problem Solving
Project Management
Business Planning
Meetings and Events
Emotional Intelligence
Human Resources
Administrative Essentials
Customer Service
Career Development
Conflict Resolution
Train the Trainer
Supervisors and Managers
Internet marketing
Communications
Team Building
Marketing
Finance
Writing
Job Search Skills
Public Speaking
Negotiation Skills
Talent Management
Brightnet Deskline 2016
BDS Preparation for Deskline 2010
Deskline 2013
Deskline 2010
Upgrading to Deskline 2010
Computer Fundamentals
Upgrading to Deskline 2007
Deskline 2003
Deskline 2002
Varlo Deskline X3
Core Essentials
Deskline 2007

Thank you so much for all of the amazing designs we received. We were so happy with so many elements that it was very hard to choose. Our top two were very hard to decide upon but we look forward to working more with both of these talents into the future. Thank you again.

Target Market(s)

Professionals, students and workers who would like to improve their skills with online training in over 500 + courses -

Industry/Entity Type

It Company

Number of Pages Required

5+ page

Font styles to use
Sans Serif

Colors
3276b5
faa54b
0355a3
fac994

Requirements
Must have
• Ideally would use Wordpress theme (Divi for example or other)
• Very smart front end
• Will upload logo soon
• (Pendlow Online Training)
• pendlowonlinetraining.edu.au
• Graphics of 'people' pretty important - with a variety of ages.
Nice to have
• Interesting page
• National presence
• A bit University looking
• Professional
• Graphics of people
• Blog
• Graphics of people
• Age range from job seekers, to business folk, etc

```html
<!DOCTYPE html>
<html lang="en">
<head>
<meta charset="utf-8">
<title>Pendlow Online Training</title>
<link href="https://fonts.googleapis.com/css2?family=Raleway:wght@400;500;600;700&family=Open+Sans:wght@400;600;700&display=swap" rel="stylesheet">
<style>
:root{
  --orange:#dd9442;
  --orange-dark:#c97f2e;
  --navy:#2b3a5b;
  --navy-deep:#24314d;
  --ink:#333a45;
  --muted:#6d7380;
  --line:#e3e5e9;
  --pale:#f2f3f5;
  --white:#ffffff;
}
*{box-sizing:border-box;margin:0;padding:0}
html,body{width:1200px;height:4945px;overflow:hidden}
body{font-family:"Open Sans",Arial,sans-serif;color:var(--ink);background:var(--white);position:relative}
h1,h2,h3,h4,.nav,.btn{font-family:"Raleway",Arial,sans-serif}
section,header,footer{position:absolute;left:0;width:1200px;overflow:hidden}
.abs{position:absolute}
.photo{position:absolute}
.btn{display:inline-block;font-size:13px;font-weight:700;letter-spacing:1px;color:var(--white);padding:10px 22px;text-transform:uppercase}
.btn-navy{background:var(--navy)}
.btn-orange{background:var(--orange)}
.sec-title{font-size:25px;font-weight:600;text-transform:uppercase;letter-spacing:1px;text-align:center}

/* header */
.site-header{top:0;height:138px;background:var(--white)}
.brand{left:160px;top:12px;width:160px;height:126px;background:var(--white);text-align:center;z-index:3}
.brand-mark{width:44px;height:44px;background:var(--navy);margin:8px auto 8px}
.brand-name{font-family:"Raleway",sans-serif;font-size:26px;font-weight:600;color:var(--navy);letter-spacing:1px}
.brand-sub{font-family:"Raleway",sans-serif;font-size:10px;color:var(--navy);letter-spacing:2px;font-weight:600}
.contact{left:590px;top:18px;font-size:14px;color:var(--ink);line-height:26px}
.contact .phone{font-size:19px;font-weight:700}
.contact svg{vertical-align:middle;margin-right:8px}
.search{left:826px;top:38px;width:236px;height:34px;border:1px solid var(--line);font-size:12px;color:#999;padding:8px 10px}
.search svg{position:absolute;right:10px;top:9px}
.nav{left:320px;top:92px;width:880px;height:42px;background:var(--orange);display:flex;align-items:center}
.nav span{color:var(--white);font-size:14px;font-weight:700;padding:0 19px;line-height:42px}
.nav .active{background:var(--navy)}

/* hero */
.hero{top:138px;height:455px;background:
  linear-gradient(90deg,rgba(40,30,22,.55) 0%,rgba(40,30,22,.15) 45%,rgba(0,0,0,0) 70%),
  radial-gradient(ellipse 180px 240px at 340px 200px,#efe2d2 0%,rgba(239,226,210,0) 100%),
  radial-gradient(ellipse 200px 260px at 860px 240px,#f4f1ee 0%,rgba(244,241,238,0) 100%),
  radial-gradient(ellipse 260px 120px at 620px 420px,#3a3d45 0%,rgba(58,61,69,0) 100%),
  linear-gradient(100deg,#5e4a3a 0%,#8c7260 25%,#c8b29c 45%,#a08a76 60%,#d9d4cf 80%,#8f8478 100%)}
.hero-copy{left:126px;top:180px;color:var(--white)}
.hero-copy .kicker{font-size:28px;font-family:"Raleway",sans-serif;font-weight:500}
.hero-copy h1{font-size:46px;font-weight:500;margin-top:2px}
.dots{left:132px;top:275px;display:flex;gap:6px}
.dots i{width:14px;height:14px;border-radius:50%;background:var(--white);display:block}
.dots i:last-child{background:transparent;border:2px solid var(--white)}

/* welcome */
.welcome{top:593px;height:330px;text-align:center}
.welcome h2{font-size:25px;font-weight:600;line-height:34px;margin-top:55px;color:var(--navy)}
.welcome p{width:720px;margin:18px auto 0;font-size:13px;line-height:22px;color:var(--muted)}
.welcome .btn{margin-top:22px}

/* courses */
.courses{top:923px;height:683px;border-top:1px solid var(--line)}
.courses h2{left:132px;top:42px;font-size:21px;font-weight:600;color:var(--orange);text-transform:uppercase}
.course{width:200px;height:230px;background:var(--white);box-shadow:0 1px 4px rgba(0,0,0,.12);border-bottom:5px solid var(--navy)}
.course .photo{left:0;top:0;width:200px;height:180px}
.course h4{position:absolute;left:14px;top:186px;font-size:14px;font-weight:700;text-transform:uppercase;color:var(--ink)}
.course small{position:absolute;left:14px;top:206px;font-size:10px;color:var(--muted)}
.courses .btn{left:534px;top:617px}

/* why */
.why{top:1606px;height:521px;background:var(--white)}
.why-photo{left:0;top:0;width:545px;height:521px;background:
  radial-gradient(ellipse 90px 110px at 330px 150px,#d9b59b 0%,rgba(217,181,155,0) 100%),
  radial-gradient(ellipse 170px 200px at 320px 380px,#1d1f24 0%,rgba(29,31,36,.6) 55%,rgba(29,31,36,0) 100%),
  radial-gradient(ellipse 140px 70px at 140px 440px,#f7f7f8 0%,rgba(247,247,248,0) 100%),
  linear-gradient(120deg,#f1f1f2 0%,#dcdde0 35%,#e9e9eb 60%,#f4f4f5 100%)}
.why h2{left:630px;top:56px;font-size:24px;font-weight:600;color:var(--navy);text-transform:uppercase}
.feature{left:560px;width:520px}
.feature .ico{position:absolute;left:0;top:0;width:52px;height:52px;border-radius:50%;background:var(--pale);display:flex;align-items:center;justify-content:center}
.feature h4{margin-left:70px;font-size:15px;font-weight:600;text-transform:uppercase;color:var(--navy)}
.feature p{margin-left:70px;margin-top:6px;font-size:12.5px;line-height:20px;color:var(--muted)}
.why .btn{left:572px;top:420px}
.badge{left:573px;top:478px;width:68px;height:68px;border-radius:50%;background:var(--navy);border:4px solid var(--white);z-index:2}

/* benefits */
.benefits{top:2127px;height:296px;background:
  radial-gradient(ellipse 260px 200px at 150px 150px,rgba(120,135,165,.35),rgba(120,135,165,0)),
  radial-gradient(ellipse 300px 200px at 1000px 140px,rgba(120,135,165,.3),rgba(120,135,165,0)),
  linear-gradient(90deg,#26345a,#33456e 50%,#26345a)}
.benefits h2{left:0;top:42px;width:1200px;color:var(--white)}
.benefit{top:115px;width:460px;color:var(--white)}
.benefit .ico{position:absolute;left:0;top:0;width:100px;height:100px;border-radius:50%;background:var(--orange);border:5px solid rgba(255,255,255,.25);display:flex;align-items:center;justify-content:center}
.benefit h4{margin-left:122px;margin-top:12px;font-size:17px;font-weight:700;text-transform:uppercase}
.benefit p{margin-left:122px;margin-top:6px;font-size:12.5px;line-height:19px;color:#d5dae6}

/* quality */
.quality{top:2423px;height:389px}
.quality-panel{left:0;top:0;width:626px;height:389px;background:linear-gradient(90deg,#d98d3c,#e39c50 70%,#dd9442)}
.quality-panel h2{position:absolute;left:165px;top:62px;font-size:26px;font-weight:500;color:var(--white);line-height:34px}
.quality-panel p{position:absolute;left:165px;top:150px;width:440px;font-size:12.5px;line-height:21px;color:#fff4e6}
.quality-panel .btn{position:absolute;left:165px;top:292px;border:1px solid var(--white);background:transparent;font-weight:500;text-transform:none;letter-spacing:0;padding:6px 16px}
.quality-photo{left:626px;top:0;width:574px;height:389px;background:
  radial-gradient(ellipse 70px 90px at 150px 110px,#d6b298 0%,rgba(214,178,152,0) 100%),
  radial-gradient(ellipse 70px 90px at 310px 150px,#d2ad92 0%,rgba(210,173,146,0) 100%),
  radial-gradient(ellipse 70px 90px at 470px 140px,#caa184 0%,rgba(202,161,132,0) 100%),
  radial-gradient(ellipse 260px 90px at 290px 330px,#c9ccd3 0%,rgba(201,204,211,0) 100%),
  radial-gradient(ellipse 120px 160px at 470px 260px,#2f333b 0%,rgba(47,51,59,0) 100%),
  linear-gradient(110deg,#e8e6e3,#f6f6f5 40%,#dedad5 70%,#eeedeb)}

/* product line */
.products{top:2812px;height:287px;background:var(--pale);text-align:center}
.products h3{margin-top:30px;font-size:17px;font-weight:700;color:var(--orange);text-transform:uppercase}
.products .wordmark{margin-top:22px;font-family:"Open Sans",sans-serif;font-size:38px;font-weight:700;color:#111}
.tiles{display:flex;justify-content:center;gap:56px;margin-top:24px}
.tiles svg{display:block}
.products p{width:760px;margin:22px auto 0;font-size:12.5px;line-height:20px;color:var(--muted)}

/* why two */
.why-two{top:3099px;height:412px;background:var(--navy)}
.why-two .photo{left:190px;top:40px;width:310px;height:372px;background:
  radial-gradient(ellipse 60px 75px at 160px 90px,#dcb79c 0%,rgba(220,183,156,0) 100%),
  radial-gradient(ellipse 90px 80px at 160px 60px,#a8784e 0%,rgba(168,120,78,0) 100%),
  radial-gradient(ellipse 150px 200px at 160px 300px,#eef1f7 0%,#d7dce7 60%,rgba(215,220,231,0) 100%),
  linear-gradient(180deg,rgba(43,58,91,0) 0%,rgba(43,58,91,0) 100%)}
.why-two .mark{left:565px;top:95px;width:44px;height:44px;border-radius:50%;background:var(--white)}
.why-two h2{left:632px;top:92px;font-size:22px;font-weight:600;color:var(--white);line-height:28px}
.why-two .item{left:565px;width:540px;color:var(--white)}
.why-two .item h4{margin-left:66px;font-size:14px;font-weight:700}
.why-two .item p{margin-left:66px;margin-top:8px;font-size:12.5px;line-height:20px;color:#d5dae6}
.why-two .item svg{position:absolute;left:0;top:0}

/* blogs */
.blogs{top:3511px;height:445px;background:var(--orange)}
.blogs h2{left:0;top:38px;width:1200px;color:var(--white)}
.post{top:102px;width:297px;height:298px;background:var(--white);text-align:center}
.post .photo{left:0;top:0;width:297px;height:145px}
.post .date{position:absolute;left:92px;top:130px;width:114px;height:26px;background:var(--orange);color:var(--white);font-size:11px;font-weight:700;line-height:26px}
.post h4{margin-top:172px;font-size:16px;font-weight:600;color:var(--orange)}
.post p{width:250px;margin:8px auto 0;font-size:11px;line-height:16px;color:var(--muted)}
.post .more{display:block;margin-top:10px;font-size:13px;font-weight:700;color:var(--ink)}

/* testimonials */
.testimonials{top:3956px;height:445px;background:linear-gradient(135deg,#f4f4f5,#e4e5e8 30%,#f4f4f5 55%,#e8e9eb 80%,#f4f4f5)}
.testimonials h2{left:0;top:36px;width:1200px;color:var(--ink)}
.avatar{position:absolute;border-radius:50%;border:4px solid var(--white);box-shadow:0 0 0 2px var(--navy),0 2px 6px rgba(0,0,0,.18)}
.quote{position:absolute;font-family:"Raleway",sans-serif;font-size:72px;font-weight:700;color:var(--orange);line-height:1}
.testimonials p{left:230px;top:300px;width:740px;text-align:center;font-size:12.5px;line-height:21px;color:var(--ink)}
.testimonials .name{left:0;top:370px;width:1200px;text-align:center;font-size:13px;color:var(--orange);font-style:italic}
.arrow{position:absolute;top:213px}

/* trusted */
.trusted{top:4401px;height:231px;background:var(--white);text-align:center}
.trusted h2{margin-top:50px;font-size:21px;font-weight:700;color:var(--navy)}
.partners{display:flex;justify-content:center;gap:10px;margin-top:26px}
.partners div{width:168px;height:66px;border:1px solid var(--line);display:flex;align-items:center;justify-content:center;gap:8px;font-family:"Open Sans",sans-serif;font-size:16px;font-weight:600;color:#4a505b}
.partners i{display:block;width:14px;height:14px;background:#4a505b}

/* footer */
.site-footer{top:4632px;height:313px;background:linear-gradient(180deg,#2b3a5b,#24314d)}
.site-footer{color:var(--white)}
.col{top:52px;width:180px}
.col h4{font-size:14px;font-weight:700;text-transform:uppercase;margin-bottom:14px}
.col li{list-style:none;font-size:12.5px;line-height:24px;color:#c9cfdc}
.foot-brand{left:855px;top:66px;width:160px;text-align:center}
.foot-brand .sq{width:48px;height:48px;background:#5a6785;margin:0 auto 10px}
.foot-brand .nm{font-family:"Raleway",sans-serif;font-size:28px;font-weight:600;color:#7d89a5}
.foot-brand .sub{font-family:"Raleway",sans-serif;font-size:10px;letter-spacing:2px;font-weight:600;color:#7d89a5}
.foot-bar{left:0;top:263px;width:1200px;height:50px;border-top:1px solid rgba(255,255,255,.12)}
.foot-bar small{position:absolute;left:145px;top:17px;font-size:11px;color:#9aa3b8}
.social{position:absolute;left:962px;top:13px;display:flex;gap:6px}
.social i{display:block;width:24px;height:24px;border-radius:50%;border:1px solid #c9cfdc}
</style>
</head>
<body>

<header class="site-header">
  <div class="abs brand"><div class="brand-mark"></div><div class="brand-name">PENDLOW</div><div class="brand-sub">ONLINE TRAINING</div></div>
  <div class="abs contact">
    <div class="phone"><svg width="16" height="16" viewBox="0 0 24 24"><path fill="#333a45" d="M6.6 10.8a15 15 0 0 0 6.6 6.6l2.2-2.2c.3-.3.7-.4 1-.2 1.1.4 2.3.6 3.6.6.6 0 1 .4 1 1V20c0 .6-.4 1-1 1A17 17 0 0 1 3 4c0-.6.4-1 1-1h3.5c.6 0 1 .4 1 1 0 1.3.2 2.5.6 3.6.1.3 0 .7-.2 1z"/></svg>1800 555 014</div>
    <div><svg width="16" height="12" viewBox="0 0 16 12"><rect width="16" height="12" fill="#333a45"/><path d="M0 0l8 6 8-6" stroke="#fff" fill="none"/></svg>info@pendlowtraining.edu.au</div>
  </div>
  <div class="abs search">Search here<svg width="14" height="14" viewBox="0 0 14 14"><circle cx="6" cy="6" r="4.5" stroke="#999" stroke-width="1.6" fill="none"/><path d="M9.5 9.5L13 13" stroke="#999" stroke-width="1.6"/></svg></div>
  <nav class="abs nav"><span class="active">HOME</span><span>ABOUT US</span><span>COURSES</span><span>TRAINING</span><span>TESTIMONIALS</span><span>BLOG</span><span>CONTACT</span></nav>
</header>

<section class="hero" role="img" aria-label="Business colleagues working together at a laptop in a bright office">
  <div class="abs hero-copy"><div class="kicker">Online Training &amp; Courses</div><h1>Process Managment</h1></div>
  <div class="abs dots"><i></i><i></i><i></i><i></i></div>
</section>

<section class="welcome">
  <h2>WELCOME TO<br>PENDLOW ONLINE TRAINING</h2>
  <p>Pendlow Online Training is one of Australia's leading provider of flexible and affordable online continuing professional development programs, with over 600 online courses now available.</p>
  <p style="margin-top:12px">Our range of self-paced online courses are delivered completely online via our e-learning system 24/7. We offer a range of popular online courses in accounting, finance, bookkeeping, management, marketing, information technology.</p>
  <span class="btn btn-navy">Read More</span>
</section>

<section class="courses">
  <h2 class="abs">Popular Courses</h2>
  <div class="abs course" style="left:132px;top:92px"><div class="photo" role="img" aria-label="Sales team meeting" style="background:radial-gradient(ellipse 50px 70px at 60px 80px,#2f343c,rgba(47,52,60,0)),radial-gradient(ellipse 60px 80px at 150px 110px,#3b4250,rgba(59,66,80,0)),linear-gradient(160deg,#f3f1ee,#d9d5cf 50%,#b8b2aa)"></div><h4>Sales Training</h4><small>Click here for more information</small></div>
  <div class="abs course" style="left:373px;top:92px"><div class="photo" role="img" aria-label="Leaders in a modern office" style="background:radial-gradient(ellipse 80px 50px at 100px 150px,#1f2530,rgba(31,37,48,0)),linear-gradient(180deg,#dfe8f2,#9fb3cb 45%,#5a6b84 75%,#2c3545)"></div><h4>Leadership</h4><small>Click here for more information</small></div>
  <div class="abs course" style="left:610px;top:92px"><div class="photo" role="img" aria-label="Colleagues reviewing a process" style="background:radial-gradient(ellipse 50px 70px at 60px 90px,#b7906f,rgba(183,144,111,0)),radial-gradient(ellipse 60px 60px at 150px 130px,#4b5260,rgba(75,82,96,0)),linear-gradient(135deg,#f4f2ef,#dcd6cf 60%,#c3bbb1)"></div><h4>Process Management</h4><small>Click here for more information</small></div>
  <div class="abs course" style="left:844px;top:92px"><div class="photo" role="img" aria-label="Safety team at a table" style="background:radial-gradient(ellipse 90px 50px at 100px 120px,#8a6f58,rgba(138,111,88,0)),radial-gradient(circle at 60px 60px,#d8c6b4,rgba(216,198,180,0) 50px),linear-gradient(135deg,#e6e8ec,#b8bdc7 60%,#9097a4)"></div><h4>Workplace Safety</h4><small>Click here for more information</small></div>
  <div class="abs course" style="left:132px;top:352px"><div class="photo" role="img" aria-label="Problem solving at a whiteboard" style="background:radial-gradient(ellipse 50px 80px at 140px 110px,#2e333b,rgba(46,51,59,0)),linear-gradient(135deg,#f5f6f7,#e0e3e7 55%,#b4bac4)"></div><h4>Problem Solving</h4><small>Click here for more information</small></div>
  <div class="abs course" style="left:373px;top:352px"><div class="photo" role="img" aria-label="Project planning workshop" style="background:radial-gradient(ellipse 60px 80px at 70px 100px,#3a414e,rgba(58,65,78,0)),radial-gradient(ellipse 70px 50px at 150px 50px,#f7f7f7,rgba(247,247,247,0)),linear-gradient(135deg,#d6dbe2,#a7b0bd 60%,#6f7a8b)"></div><h4>Project Management</h4><small>Click here for more information</small></div>
  <div class="abs course" style="left:610px;top:352px"><div class="photo" role="img" aria-label="Gears representing process flow" style="background:radial-gradient(circle at 60px 70px,#7fa4cf,rgba(127,164,207,0) 45px),radial-gradient(circle at 140px 110px,#4f78a8,rgba(79,120,168,0) 55px),linear-gradient(135deg,#c7d5e6,#6f87a6 60%,#34496a)"></div><h4>Process Management</h4><small>Click here for more information</small></div>
  <div class="abs course" style="left:844px;top:352px"><div class="photo" role="img" aria-label="Meeting around a conference table" style="background:radial-gradient(ellipse 100px 40px at 100px 140px,#6e5441,rgba(110,84,65,0)),radial-gradient(ellipse 40px 50px at 60px 80px,#d3b49a,rgba(211,180,154,0)),radial-gradient(ellipse 40px 50px at 140px 80px,#c9a98e,rgba(201,169,142,0)),linear-gradient(135deg,#e8e2da,#bfb3a5 60%,#8c7e70)"></div><h4>Meetings and Events</h4><small>Click here for more information</small></div>
  <span class="abs btn btn-orange">View More</span>
</section>

<section class="why">
  <div class="photo why-photo" role="img" aria-label="Smiling businesswoman with glasses working at a laptop"></div>
  <h2 class="abs">Why Pendlow Online</h2>
  <div class="abs feature" style="top:120px"><div class="ico"><svg width="24" height="20" viewBox="0 0 24 20"><rect x="1" y="1" width="22" height="14" fill="none" stroke="#dd9442" stroke-width="2"/><path d="M8 19h8M12 15v4" stroke="#dd9442" stroke-width="2"/></svg></div><h4>Flexible</h4><p>Pendlow provide an online learning platform which fits into your lifestyle and work commitments. You study anywhere, anytime!</p></div>
  <div class="abs feature" style="top:210px"><div class="ico"><svg width="22" height="22" viewBox="0 0 22 22"><path d="M11 1l3 7h7l-6 5 2 8-6-4-6 4 2-8-6-5h7z" fill="#dd9442"/></svg></div><h4>Value</h4><p>Our innovative online training approach allows us to deliver exceptional training in over 600 industry endorsed courses at affordable prices with no hidden extras. Courses may be tax deductable - check with your Tax Agent today!</p></div>
  <div class="abs feature" style="top:320px"><div class="ico"><svg width="22" height="20" viewBox="0 0 22 20"><rect x="1" y="5" width="20" height="14" fill="#dd9442"/><rect x="7" y="1" width="8" height="5" fill="none" stroke="#dd9442" stroke-width="2"/></svg></div><h4 style="text-transform:none">Experience</h4><p>Pendlow is one of Australia's largest and leading provider of training services in nationally.</p></div>
  <span class="abs btn btn-navy">More About Us</span>
  <div class="abs badge"></div>
</section>

<section class="benefits">
  <h2 class="abs sec-title">Benefits of Further Training</h2>
  <div class="abs benefit" style="left:145px"><div class="ico"><svg width="40" height="40" viewBox="0 0 40 40"><path d="M6 34L34 6M20 6h14v14" stroke="#fff" stroke-width="4" fill="none"/></svg></div><h4>Skill Up</h4><p>Pendlow provide an online learning platform which fits into your lifestyle and work commitments. You study anywhere, anytime!</p></div>
  <div class="abs benefit" style="left:625px"><div class="ico"><svg width="40" height="40" viewBox="0 0 40 40"><rect x="6" y="6" width="28" height="28" rx="3" fill="none" stroke="#fff" stroke-width="3"/><path d="M12 26l7-7 5 5 6-8" stroke="#fff" stroke-width="3" fill="none"/></svg></div><h4>Career Planning</h4><p>Our innovative online training approach allows us to deliver exceptional training in over 600 industry endorsed courses at affordable prices.</p></div>
</section>

<section class="quality">
  <div class="photo quality-panel">
    <h2>Quality Training That<br>Gets Results</h2>
    <p>Training brings direct benefits to both employees and the organisation. Training and learning opportunities are an investment that helps employees develop their careers while giving your business a competitive advantage. By investing in their training, staff feel valued and in turn develop stronger.</p>
    <span class="btn">Learn More</span>
  </div>
  <div class="photo quality-photo" role="img" aria-label="Cheerful office team gathered around a laptop"></div>
</section>

<section class="products">
  <h3>Pendlow Specialise in Online Brightnet Product Training</h3>
  <div class="wordmark">Brightnet</div>
  <div class="tiles">
    <svg width="52" height="56" viewBox="0 0 52 56"><path d="M4 2h32l12 12v40H4z" fill="none" stroke="#4a505b" stroke-width="3"/><path d="M12 22h28M12 30h28M12 38h20" stroke="#4a505b" stroke-width="3"/></svg>
    <svg width="52" height="56" viewBox="0 0 52 56"><rect x="3" y="3" width="46" height="50" fill="none" stroke="#4a505b" stroke-width="3"/><path d="M3 18h46M3 33h46M19 3v50M34 3v50" stroke="#4a505b" stroke-width="2.5"/></svg>
    <svg width="52" height="56" viewBox="0 0 52 56"><rect x="3" y="6" width="46" height="34" fill="none" stroke="#4a505b" stroke-width="3"/><path d="M26 40v12M16 52h20" stroke="#4a505b" stroke-width="3"/><path d="M12 32l9-10 7 6 12-12" stroke="#4a505b" stroke-width="3" fill="none"/></svg>
    <svg width="52" height="56" viewBox="0 0 52 56"><rect x="3" y="3" width="46" height="50" fill="none" stroke="#4a505b" stroke-width="3"/><path d="M12 44V28M22 44V18M32 44V24M42 44V12" stroke="#4a505b" stroke-width="5"/></svg>
    <svg width="52" height="56" viewBox="0 0 52 56"><ellipse cx="26" cy="10" rx="21" ry="7" fill="none" stroke="#4a505b" stroke-width="3"/><path d="M5 10v36c0 4 9 7 21 7s21-3 21-7V10M5 28c0 4 9 7 21 7s21-3 21-7" fill="none" stroke="#4a505b" stroke-width="3"/></svg>
    <svg width="52" height="56" viewBox="0 0 52 56"><rect x="3" y="10" width="46" height="36" fill="none" stroke="#4a505b" stroke-width="3"/><path d="M3 10l23 20 23-20" stroke="#4a505b" stroke-width="3" fill="none"/></svg>
  </div>
  <p>Ullamcorper nec eget tempor cursus neque mi consectetuer mi a ultrices massa est sed nisl. Class aptent taciti sociosqu ad litora torquent per conubia nostra per inceptos.</p>
</section>

<section class="why-two">
  <svg class="abs" style="left:0;top:0" width="1200" height="120" viewBox="0 0 1200 120" preserveAspectRatio="none"><path d="M0 0H1200V40Q600 160 0 40Z" fill="#f2f3f5"/></svg>
  <div class="photo" role="img" aria-label="Confident businesswoman with arms crossed"></div>
  <div class="abs mark"></div>
  <h2 class="abs">WHY PENDLOW<br>ONLINE?</h2>
  <div class="abs item" style="top:180px"><svg width="44" height="30" viewBox="0 0 44 30"><path d="M4 8h34l-6-6M40 22H6l6 6" stroke="#fff" stroke-width="2.5" fill="none"/></svg><h4>FLEXIBLE</h4><p>Pendlow provide an online learning platform which fits into your lifestyle and work commitments. You study anywhere, anytime!</p></div>
  <div class="abs item" style="top:275px"><svg width="40" height="30" viewBox="0 0 40 30"><rect x="3" y="3" width="34" height="24" rx="2" fill="none" stroke="#fff" stroke-width="2.5"/><path d="M3 11h34" stroke="#fff" stroke-width="2.5"/></svg><h4>VALUE</h4><p>Pendlow provide an online learning platform which fits into your lifestyle and work commitments. You study anywhere, anytime!</p></div>
</section>

<section class="blogs">
  <h2 class="abs sec-title">Latest Blogs</h2>
  <div class="abs post" style="left:132px"><div class="photo" role="img" aria-label="Team meeting at a whiteboard" style="background:radial-gradient(ellipse 40px 55px at 70px 80px,#2f343d,rgba(47,52,61,0)),radial-gradient(ellipse 40px 55px at 220px 90px,#3b4250,rgba(59,66,80,0)),radial-gradient(ellipse 80px 40px at 150px 40px,#ffffff,rgba(255,255,255,0)),linear-gradient(135deg,#e9ecf0,#c3cad4 60%,#97a1b0)"></div><span class="date">02 MAY 2016</span><h4>Aculis facilisis massa</h4><p>Etiam eu urna sed porta. Suspendisse quam leo molestie sed luctus quis feugiat in pede. Fusce tellus sed metus augue.</p><span class="more">Read More</span></div>
  <div class="abs post" style="left:452px"><div class="photo" role="img" aria-label="Businesswoman in a bright office" style="background:radial-gradient(ellipse 45px 60px at 140px 60px,#d7b59a,rgba(215,181,154,0)),radial-gradient(ellipse 70px 60px at 140px 140px,#2a2d33,rgba(42,45,51,0)),linear-gradient(135deg,#f5f4f2,#e1ddd8 60%,#c7c0b7)"></div><span class="date">02 MAY 2016</span><h4>Aculis facilisis massa</h4><p>Etiam eu urna sed porta. Suspendisse quam leo molestie sed luctus quis feugiat in pede. Fusce tellus sed metus augue.</p><span class="more">Read More</span></div>
  <div class="abs post" style="left:772px"><div class="photo" role="img" aria-label="Presenter with a chart" style="background:radial-gradient(ellipse 60px 45px at 210px 60px,#3f6ea6,rgba(63,110,166,0)),radial-gradient(ellipse 40px 60px at 80px 100px,#373c46,rgba(55,60,70,0)),linear-gradient(135deg,#eef1f5,#c9d2de 60%,#8d9bb0)"></div><span class="date">02 MAY 2016</span><h4>Aculis facilisis massa</h4><p>Etiam eu urna sed porta. Suspendisse quam leo molestie sed luctus quis feugiat in pede. Fusce tellus sed metus augue.</p><span class="more">Read More</span></div>
</section>

<section class="testimonials">
  <h2 class="abs sec-title">Our Testimonials</h2>
  <div class="avatar" role="img" aria-label="Client portrait" style="left:366px;top:150px;width:120px;height:120px;background:radial-gradient(circle at 50% 40%,#d9bba2,#8a6c55 70%,#4a3d33)"></div>
  <div class="avatar" role="img" aria-label="Client portrait" style="left:448px;top:140px;width:140px;height:140px;background:radial-gradient(circle at 50% 42%,#e0c3a9,#9c7a5f 65%,#3e3a3b)"></div>
  <div class="avatar" role="img" aria-label="Client portrait" style="left:528px;top:122px;width:168px;height:168px;background:radial-gradient(circle at 50% 42%,#e6c8ad,#a78266 60%,#2f3442);z-index:2"></div>
  <div class="avatar" role="img" aria-label="Client portrait" style="left:636px;top:140px;width:140px;height:140px;background:radial-gradient(circle at 50% 42%,#dfc0a5,#8f6f58 65%,#5a4a40)"></div>
  <div class="avatar" role="img" aria-label="Client portrait" style="left:738px;top:150px;width:120px;height:120px;background:radial-gradient(circle at 50% 40%,#e3c7ae,#a0846d 70%,#6b5a4d)"></div>
  <span class="quote" style="left:255px;top:175px">&ldquo;</span>
  <span class="quote" style="left:915px;top:175px">&rdquo;</span>
  <svg class="arrow" style="left:80px" width="20" height="34" viewBox="0 0 20 34"><path d="M18 2L3 17l15 15" stroke="#2b3a5b" stroke-width="3" fill="none"/></svg>
  <svg class="arrow" style="left:1100px" width="20" height="34" viewBox="0 0 20 34"><path d="M2 2l15 15L2 32" stroke="#2b3a5b" stroke-width="3" fill="none"/></svg>
  <p class="abs">I want to say a huge thank you for the course and knowledge I came away with. I have secured a fantastic job after my first application! Such good value for money but I would highly recommend it. I'm a mature age person so it's never too late to up-skill yourself to get what you deserve!</p>
  <div class="abs name">~ Mara Lindqvist</div>
</section>

<section class="trusted">
  <h2>TRUSTED BY</h2>
  <div class="partners">
    <div><i></i>Brightnet</div>
    <div>Norvale</div>
    <div>Steady Reach</div>
    <div>Quillex</div>
    <div>Tidewell</div>
  </div>
</section>

<footer class="site-footer">
  <div class="abs col" style="left:145px"><h4>Company</h4><ul><li>Home</li><li>About Us</li><li>Why Choose Us</li><li>Services Provides</li></ul></div>
  <div class="abs col" style="left:333px"><h4>Services</h4><ul><li>Communication</li><li>Open Source</li><li>Integration &amp; System</li><li>Mobile &amp; IT</li></ul></div>
  <div class="abs col" style="left:527px"><h4>Resources</h4><ul><li>Mauris vel lacus</li><li>Alias felis vestibulum</li><li>Volutpat imperdiet at</li><li>Cum sociis natoque</li></ul></div>
  <div class="abs col" style="left:733px"><h4>Why Us</h4><ul><li>Customers</li><li>Team</li><li>FAQ</li><li>Contact</li></ul></div>
  <div class="abs foot-brand"><div class="sq"></div><div class="nm">PENDLOW</div><div class="sub">ONLINE TRAINING</div></div>
  <div class="abs foot-bar"><small>&copy; 2016 Company Name. All rights reserved. Term of Use</small><div class="social"><i></i><i></i><i></i><i></i><i></i></div></div>
</footer>

</body>
</html>
```